Create our new Brightcup Coffee Syrup Label designs. A delicious job!

Design a front label for a range of coffee syrup flavours. The brand is 'Brightcup Coffee Syrups'. The flavours, vanilla, hazelnut and caramel.
Our coffee syrups are made with only natural colours and flavours and are positioned in the popular premium space in Australian and international cafes.
The labels will be applied to 750 ml Boston Bottles (see attached image).
Given that coffee syrups are often positioned in high visibility locations in cafes, they can be considered as objects of functional beauty.
This range is a sub brand for our company and I have attached our main brand images in the flavours we want. we want this brand to look different to this Marlowe branded range, but included the image to show what we are currently doing in this space.
The different flavours can be identified by a combination of colour and text, which may be a line or section of the otherwise same overall design.
We are going to do a 2 part label with the front just carrying Brand and flavour descriptors plus 750 ml.
Total Bottle height is 240 mm bottle width is 70 mm

Target Market(s)

Cafe patrons, primarily women, 18-35, Middle class in terms of economics, regular cafe patrons. Who are looking for a guilt free treat in their busy day.

Logo Text

Brightcup Coffee Syrups Vanilla (or Hazelnut, or Caramel) 750 ml

Logo styles of interest
Pictorial/Combination Logo
Font styles to use
Sans Serif

Colors

Designer to choose colors to be used in the design.

Requirements
Must have
• A clear design, which is a combination of font and image. it needs to be legible from up to 2m away (across a counter in a cafe).
• We would like to see a device, which may be a gold drop, that may be the 'brightcup' meant to the coffee.
• The way our coffee syrups are used is by adding a small amount (15 ml) to a cup
• of coffee, this adds both flavour and sweetness to the overall coffee experience, and cafes charge a premium for this service. We want our package to show this will be a great thing to do.
• We have a few options in terms of Label stock. We can print on a foil, that will allow a metallic sheen to come through the colours (see example of the Marlowe branded bottles.
Nice to have
• We are looking for a modern, clean and distinctive look and feel to this range.
• I have added a key line for the front and back label, however we can create a different label die line should the design warrant that. Note this is just for the front label.
Should not have
• Difficult to read fonts or imagery that is not clear.
• Should look different to the Marlowe branded product range.

```html
<!DOCTYPE html>
<html lang="en">
<head>
<meta charset="utf-8">
<title>Brightcup Coffee Syrups – Front Label</title>
<link rel="stylesheet" href="https://fonts.googleapis.com/css2?family=Montserrat:wght@500;700;800&display=swap">
<style>
  :root {
    --bg-light: #d2bca7;
    --bg-mid: #b3957e;
    --bg-dark: #7d5c48;
    --panel-light: #cfb9a4;
    --panel-dark: #a88a74;
    --band-light: #c8733a;
    --band-dark: #7a3f1c;
    --bean-light: #7a4a2c;
    --bean-dark: #24140b;
    --name-ink: #fbf6ef;
    --word-ink: #c0672e;
    --rule-ink: #8c5a3a;
    --drop-gold: #d9a640;
    --flavour-ink: #ffffff;
  }
  * { margin: 0; padding: 0; box-sizing: border-box; }
  html, body { width: 1200px; height: 800px; overflow: hidden; background: var(--bg-dark); }
  .label {
    position: relative;
    width: 1200px;
    height: 800px;
    overflow: hidden;
    background: radial-gradient(ellipse 70% 65% at 50% 35%, var(--bg-light) 0%, var(--bg-mid) 55%, var(--bg-dark) 100%);
    font-family: "Montserrat", Arial, sans-serif;
  }
  .label__backdrop, .brand__arch { position: absolute; left: 0; top: 0; width: 1200px; height: 800px; }
  .brand__name-text {
    font-family: "Montserrat", Arial, sans-serif;
    font-weight: 800;
    font-size: 104px;
    letter-spacing: 2px;
    fill: var(--name-ink);
  }
  .brand__rule { position: absolute; height: 2px; background: var(--rule-ink); }
  .brand__rule--top-left { left: 357px; top: 316px; width: 204px; }
  .brand__rule--top-right { left: 680px; top: 314px; width: 200px; }
  .brand__rule--bottom-left { left: 357px; top: 400px; width: 204px; }
  .brand__rule--bottom-right { left: 680px; top: 404px; width: 200px; }
  .brand__word {
    position: absolute;
    top: 326px;
    font-size: 58px;
    font-weight: 700;
    line-height: 64px;
    color: var(--word-ink);
    text-align: center;
  }
  .brand__word--left { left: 357px; width: 204px; }
  .brand__word--right { left: 680px; width: 200px; }
  .brand__drop {
    position: absolute;
    left: 588px; top: 334px;
    width: 50px; height: 50px;
    border-radius: 50%;
    background: var(--drop-gold);
  }
  .flavour {
    position: absolute;
    left: 0; width: 1200px;
    top: 424px;
    text-align: center;
    font-size: 26px;
    font-weight: 500;
    color: var(--flavour-ink);
  }
  .volume {
    position: absolute;
    left: 0; width: 1200px;
    top: 464px;
    text-align: center;
    font-size: 22px;
    font-weight: 500;
    letter-spacing: 1px;
    color: var(--flavour-ink);
  }
</style>
</head>
<body>
  <main class="label">
    <svg class="label__backdrop" viewBox="0 0 1200 800" xmlns="http://www.w3.org/2000/svg">
      <defs>
        <linearGradient id="panel-shade" x1="0" y1="0" x2="0" y2="1">
          <stop offset="0" stop-color="var(--panel-light)" stop-opacity="0"/>
          <stop offset="1" stop-color="var(--panel-dark)" stop-opacity="0.6"/>
        </linearGradient>
        <linearGradient id="band-shade" x1="0" y1="0" x2="1" y2="0.3">
          <stop offset="0" stop-color="var(--band-dark)"/>
          <stop offset="0.35" stop-color="var(--band-light)"/>
          <stop offset="0.7" stop-color="var(--band-light)"/>
          <stop offset="1" stop-color="var(--band-dark)"/>
        </linearGradient>
        <radialGradient id="bean-shade" cx="0.5" cy="0.4" r="0.8">
          <stop offset="0" stop-color="var(--bean-light)"/>
          <stop offset="1" stop-color="var(--bean-dark)"/>
        </radialGradient>
      </defs>
      <path class="label__panel-shadow" d="M0 330 Q 300 500 600 520 Q 900 530 1200 420 L1200 800 L0 800 Z" fill="url(#panel-shade)"/>
      <path class="label__band" d="M0 335 Q 260 500 620 525 Q 940 540 1200 430 L1200 520 Q 900 600 600 612 Q 250 600 0 520 Z" fill="url(#band-shade)"/>
      <path class="label__beans" role="img" aria-label="Photograph of roasted coffee beans" d="M0 520 Q 250 600 600 615 Q 900 605 1200 505 L1200 800 L0 800 Z" fill="url(#bean-shade)"/>
    </svg>

    <header class="brand">
      <svg class="brand__arch" viewBox="0 0 1200 800" xmlns="http://www.w3.org/2000/svg">
        <path id="name-arc" d="M300 285 Q 600 120 900 285" fill="none"/>
        <text class="brand__name-text"><textPath href="#name-arc" startOffset="50%" text-anchor="middle">Brightcup</textPath></text>
      </svg>
      <span class="brand__rule brand__rule--top-left"></span>
      <span class="brand__rule brand__rule--top-right"></span>
      <span class="brand__word brand__word--left">Coffee</span>
      <span class="brand__drop"></span>
      <span class="brand__word brand__word--right">Syrups</span>
      <span class="brand__rule brand__rule--bottom-left"></span>
      <span class="brand__rule brand__rule--bottom-right"></span>
    </header>

    <p class="flavour">Vanilla (or Hazelnut, or Caramel)</p>
    <p class="volume">750 ml</p>
  </main>
</body>
</html>
```